Harmony Four Showcase
Date: Sunday Oct 2, 2022
When: 2-4 p.m.
Location: Brindle9 Alehouse
413 Marigold Wy #200, Sacramento, CA 95821
Tickets: www.Ticketwisp.example
General seating: $15 for adults and $10 for students

```html
<!DOCTYPE html>
<html lang="en">
<head>
<meta charset="utf-8">
<title>Harmony Four Showcase</title>
<link rel="stylesheet" href="https://fonts.googleapis.com/css2?family=Montserrat:wght@400;500;800&family=Sacramento&display=swap">
<style>
  :root {
    --page-bg: #e6e5e1;
    --poster-black: #050404;
    --title-orange: #ff6a00;
    --neon-core: #d9f3ff;
    --neon-glow: #34aaff;
    --icon-red: #d62a2a;
    --detail-white: #ffffff;
    --band-red: #b81c1c;
    --band-dark: #2a0606;
    --ticket-gold: #e8952b;
  }
  * { margin: 0; padding: 0; box-sizing: border-box; }
  html, body {
    width: 1200px; height: 1200px; overflow: hidden;
    background: var(--page-bg);
  }
  .poster {
    position: absolute; left: 136px; top: 0;
    width: 928px; height: 1200px;
    background: var(--poster-black);
    overflow: hidden;
    font-family: "Montserrat", sans-serif;
  }
  .hero-photo {
    position: absolute; left: 0; top: 0; width: 928px; height: 600px;
    background:
      radial-gradient(ellipse 45% 55% at 78% 18%, rgba(214,150,70,.85), rgba(120,70,30,.4) 55%, transparent 80%),
      radial-gradient(ellipse 30% 40% at 35% 30%, rgba(200,150,130,.55), transparent 75%),
      radial-gradient(ellipse 25% 35% at 8% 30%, rgba(190,110,50,.7), transparent 80%),
      linear-gradient(180deg, #4a4150 0%, #3a2f35 45%, #140f10 80%, var(--poster-black) 100%);
  }
  .halftone-left {
    position: absolute; left: 0; top: 430px; width: 360px; height: 420px;
    background: radial-gradient(ellipse 60% 55% at 20% 45%, rgba(150,80,20,.55), transparent 75%);
  }
  .halftone-right {
    position: absolute; right: 0; top: 700px; width: 560px; height: 420px;
    background: radial-gradient(ellipse 60% 55% at 75% 55%, rgba(120,25,15,.55), transparent 75%);
  }
  .title-line {
    position: absolute; left: 124px;
    font-weight: 800; font-size: 150px; line-height: 1;
    letter-spacing: -4px;
    color: var(--title-orange);
  }
  .title-harmony { top: 400px; }
  .title-four { top: 556px; }
  .title-script {
    position: absolute; left: 255px; top: 692px;
    font-family: "Sacramento", cursive;
    font-size: 150px; line-height: 1;
    color: var(--neon-core);
    text-shadow: 0 0 4px var(--neon-glow), 0 0 10px var(--neon-glow), 0 0 22px var(--neon-glow);
  }
  .info-icon { position: absolute; }
  .icon-calendar { left: 83px; top: 873px; }
  .icon-clock { left: 429px; top: 880px; }
  .icon-pin { left: 801px; top: 882px; }
  .info-date, .info-time {
    position: absolute; top: 982px;
    color: var(--detail-white);
    font-weight: 400; font-size: 38px; line-height: 1.2;
    letter-spacing: 1px;
  }
  .info-date { left: 62px; }
  .info-time { left: 382px; }
  .info-venue {
    position: absolute; right: 63px; top: 996px;
    color: var(--detail-white);
    font-weight: 400; font-size: 18px; line-height: 27px;
    text-align: right; letter-spacing: .5px;
  }
  .info-seating {
    position: absolute; left: 62px; top: 1080px;
    color: var(--ticket-gold);
    font-weight: 500; font-size: 18px; line-height: 1.2;
    letter-spacing: .5px;
  }
  .ticket-band {
    position: absolute; left: 0; bottom: 0; width: 928px; height: 84px;
    background: linear-gradient(90deg, var(--band-dark) 0%, var(--band-red) 50%, var(--band-dark) 100%);
    display: flex; align-items: center; justify-content: center;
  }
  .ticket-text {
    font-weight: 800; font-size: 40px;
    color: var(--ticket-gold);
  }
</style>
</head>
<body>
  <main class="poster">
    <div class="hero-photo" role="img" aria-label="Photo of a singer performing at a vintage microphone with golden sparkles in warm stage light"></div>
    <div class="halftone-left" role="img" aria-label="Orange halftone dot decoration"></div>
    <div class="halftone-right" role="img" aria-label="Red halftone dot decoration"></div>

    <h1>
      <span class="title-line title-harmony">Harmony</span>
      <span class="title-line title-four">Four</span>
      <span class="title-script">Showcase</span>
    </h1>

    <svg class="info-icon icon-calendar" width="68" height="70" viewBox="0 0 68 70" aria-hidden="true">
      <rect x="3" y="10" width="62" height="57" fill="none" stroke="var(--icon-red)" stroke-width="6"/>
      <rect x="3" y="10" width="62" height="12" fill="var(--icon-red)"/>
      <rect x="15" y="2" width="6" height="14" rx="2" fill="var(--icon-red)"/>
      <rect x="47" y="2" width="6" height="14" rx="2" fill="var(--icon-red)"/>
      <g fill="var(--icon-red)">
        <rect x="14" y="30" width="7" height="6"/><rect x="25" y="30" width="7" height="6"/><rect x="36" y="30" width="7" height="6"/><rect x="47" y="30" width="7" height="6"/>
        <rect x="14" y="40" width="7" height="6"/><rect x="25" y="40" width="7" height="6"/><rect x="36" y="40" width="7" height="6"/><rect x="47" y="40" width="7" height="6"/>
        <rect x="14" y="50" width="7" height="6"/><rect x="25" y="50" width="7" height="6"/><rect x="36" y="50" width="7" height="6"/><rect x="47" y="50" width="7" height="6"/>
      </g>
    </svg>

    <svg class="info-icon icon-clock" width="68" height="68" viewBox="0 0 68 68" aria-hidden="true">
      <circle cx="34" cy="34" r="29" fill="none" stroke="var(--icon-red)" stroke-width="6"/>
      <path d="M34 18 V36 L44 44" fill="none" stroke="var(--icon-red)" stroke-width="5" stroke-linecap="round"/>
    </svg>

    <svg class="info-icon icon-pin" width="46" height="62" viewBox="0 0 46 62" aria-hidden="true">
      <path d="M23 0 C10 0 0 10 0 23 C0 39 23 62 23 62 C23 62 46 39 46 23 C46 10 36 0 23 0 Z M23 15 A8 8 0 1 1 23 31 A8 8 0 1 1 23 15 Z" fill="var(--icon-red)" fill-rule="evenodd"/>
    </svg>

    <p class="info-date">SUNDAY<br>OCT 2, 2022</p>
    <p class="info-time">2-4 p.m.</p>
    <p class="info-venue">Brindle9 Alehouse 413<br>Marigold Wy #200,<br>Sacramento,<br>CA 95821</p>
    <p class="info-seating">General seating: $15 adults · $10 students</p>

    <div class="ticket-band">
      <p class="ticket-text">Tickets: www.Ticketwisp.example</p>
    </div>
  </main>
</body>
</html>
```